Eco-Friendly Wheat Straw Drinking Straw Packaging Design Contest

We are seeking talented designers to create a standout packaging design for our eco-friendly wheat straw drinking straws. Our product is an environmentally conscious alternative to plastic and paper straws. We want a design that not only reflects our brand values of sustainability and health but also stands out on store shelves. Please see attached file for detailed brief and requirements.
Updates

Colors
00AB8E
00BBA5
67D7C9
C6EFE9
E9F9F6
59FF00
82FF00
B8FF75
E3FFCB
F4FFEA
FFF300
FFF600
FEFA6F
FFFEC7
FFFEE8

Requirements
Must have
• Clean, modern, and visually appealing design focusing on eco-friendliness and health. Use of earthy colors like green, beige, or brown. Final design should be in Turkish. Please see the brief file attached for further details.
Nice to have
• Scalable design that can be adapted for various packaging sizes. Incorporate creative illustrations or graphics representing wheat, nature, or sustainability.
Should not have
• Avoid overly complex or cluttered designs. Simplicity and clarity are key. Do not use bright or flashy colors that do not align with the natural and eco-friendly theme of the product. Avoid using English text in the final design. All text should be in Turkish, as the product will be marketed locally.

```html
<!DOCTYPE html>
<html lang="tr">
<head>
<meta charset="utf-8">
<title>Tera Doğal Buğday Sapından Pipet</title>
<link href="https://fonts.googleapis.com/css2?family=Cinzel:wght@500&family=Montserrat:wght@500;600;800&family=Oswald:wght@700&display=swap" rel="stylesheet">
<style>
  :root {
    --bg: #ece1cf;
    --kraft: #c9b190;
    --cream: #f4f5e7;
    --green: #3f8a3d;
    --brown: #96503f;
    --yellow: #f4cb2c;
    --ink: #2b2b2b;
  }
  * { margin: 0; padding: 0; box-sizing: border-box; }
  html, body { width: 800px; height: 1200px; overflow: hidden; }
  body {
    background: radial-gradient(ellipse at center, #f4ebdf 0%, var(--bg) 70%);
    position: relative;
    font-family: "Montserrat", sans-serif;
  }
  .label {
    position: absolute; left: 140px; top: 210px; width: 520px; height: 780px;
    background: var(--kraft);
    border-radius: 44px;
    overflow: hidden;
    box-shadow: 0 14px 22px rgba(90, 70, 40, 0.25);
  }
  .brand-panel {
    position: absolute; left: 57px; top: 0; width: 404px; height: 317px;
    background: var(--cream);
  }
  .brand-panel .edge { position: absolute; left: 0; bottom: -6px; width: 404px; height: 8px; }
  .brand-tagline {
    position: absolute; top: 46px; width: 100%; text-align: center;
    font-family: "Cinzel", serif; font-size: 19px; letter-spacing: 9px;
    color: var(--green); padding-left: 9px;
  }
  .brand-name {
    position: absolute; top: 86px; left: 0; width: 100%;
    display: flex; align-items: center; justify-content: center; gap: 14px;
  }
  .brand-name .dot {
    width: 76px; height: 76px; border-radius: 50%;
    border: 4px solid var(--green);
  }
  .brand-name span {
    font-family: "Montserrat", sans-serif; font-weight: 600; font-size: 56px;
    color: var(--green); letter-spacing: 1px;
  }
  .product-title {
    position: absolute; top: 198px; width: 100%; text-align: center;
    font-family: "Oswald", sans-serif; font-weight: 700; font-size: 42px;
    line-height: 48px; color: var(--green); letter-spacing: 0.5px;
  }
  .slogan {
    position: absolute; left: 60px; top: 338px;
    font-weight: 800; font-size: 39px; line-height: 52px; color: var(--brown);
    letter-spacing: -0.3px;
  }
  .features {
    position: absolute; left: 60px; top: 478px; list-style: none;
  }
  .features li {
    display: flex; align-items: center; gap: 12px;
    font-size: 12.5px; font-weight: 500; color: var(--brown);
    height: 24.5px;
  }
  .features svg { width: 16px; height: 16px; }
  .wheat-art {
    position: absolute; left: 253px; top: 427px; width: 267px; height: 353px;
    background: linear-gradient(160deg, rgba(201,177,144,0) 0%, #d8b58e 35%, #c9976c 70%, #b58257 100%);
    clip-path: polygon(35% 0, 100% 0, 100% 100%, 60% 100%, 0 45%, 30% 30%);
  }
  .badge { position: absolute; left: 60px; top: 590px; width: 140px; height: 150px; }
  .badge .size {
    position: absolute; left: 48px; top: 5px; width: 44px; height: 52px;
    background: var(--yellow); border-radius: 12px 12px 4px 4px;
    text-align: center; color: var(--ink); line-height: 1; z-index: 2;
  }
  .badge .size b { display: block; font-weight: 800; font-size: 21px; margin-top: 6px; }
  .badge .size small { display: block; font-size: 15px; font-weight: 500; margin-top: 1px; }
  .badge .count {
    position: absolute; left: 32px; top: 42px; width: 76px; height: 76px;
    border-radius: 50%; background: var(--brown); color: #fff;
    text-align: center; line-height: 1; z-index: 1;
  }
  .badge .count b { display: block; font-weight: 800; font-size: 20px; margin-top: 20px; }
  .badge .count small { font-size: 18px; font-weight: 500; }
  .badge svg.arc { position: absolute; left: 0; top: 0; z-index: 0; }
</style>
</head>
<body>
  <div class="label">
    <div class="brand-panel">
      <div class="brand-tagline">TERA DOĞAL TARIM</div>
      <div class="brand-name"><div class="dot"></div><span>TERA</span></div>
      <h1 class="product-title">DOĞAL BUĞDAY<br>SAPINDAN&nbsp; PIPET</h1>
      <svg class="edge" viewBox="0 0 404 8" preserveAspectRatio="none">
        <path d="M0 0 H404 V3 Q401 8 398 3 Q395 8 392 3 Q389 8 386 3 Q383 8 380 3 Q377 8 374 3 Q371 8 368 3 Q365 8 362 3 Q359 8 356 3 Q353 8 350 3 Q347 8 344 3 Q341 8 338 3 Q335 8 332 3 Q329 8 326 3 Q323 8 320 3 Q317 8 314 3 Q311 8 308 3 Q305 8 302 3 Q299 8 296 3 Q293 8 290 3 Q287 8 284 3 Q281 8 278 3 Q275 8 272 3 Q269 8 266 3 Q263 8 260 3 Q257 8 254 3 Q251 8 248 3 Q245 8 242 3 Q239 8 236 3 Q233 8 230 3 Q227 8 224 3 Q221 8 218 3 Q215 8 212 3 Q209 8 206 3 Q203 8 200 3 Q197 8 194 3 Q191 8 188 3 Q185 8 182 3 Q179 8 176 3 Q173 8 170 3 Q167 8 164 3 Q161 8 158 3 Q155 8 152 3 Q149 8 146 3 Q143 8 140 3 Q137 8 134 3 Q131 8 128 3 Q125 8 122 3 Q119 8 116 3 Q113 8 110 3 Q107 8 104 3 Q101 8 98 3 Q95 8 92 3 Q89 8 86 3 Q83 8 80 3 Q77 8 74 3 Q71 8 68 3 Q65 8 62 3 Q59 8 56 3 Q53 8 50 3 Q47 8 44 3 Q41 8 38 3 Q35 8 32 3 Q29 8 26 3 Q23 8 20 3 Q17 8 14 3 Q11 8 8 3 Q5 8 2 3 L0 3 Z" fill="var(--cream)"/>
      </svg>
    </div>

    <p class="slogan">Topraktan Masaya,<br>Masadan Toprağa!</p>

    <ul class="features">
      <li><svg viewBox="0 0 16 16"><circle cx="8" cy="8" r="8" fill="var(--brown)"/><path d="M4.5 8.2 7 10.6 11.8 5.4" stroke="#fff" stroke-width="2" fill="none"/></svg>Doğada çözünür.</li>
      <li><svg viewBox="0 0 16 16"><circle cx="8" cy="8" r="8" fill="var(--brown)"/><path d="M4.5 8.2 7 10.6 11.8 5.4" stroke="#fff" stroke-width="2" fill="none"/></svg>Sıvı içerisinde erimez, yumuşamaz.</li>
      <li><svg viewBox="0 0 16 16"><circle cx="8" cy="8" r="8" fill="var(--brown)"/><path d="M4.5 8.2 7 10.6 11.8 5.4" stroke="#fff" stroke-width="2" fill="none"/></svg>Kimyasal içermez.</li>
      <li><svg viewBox="0 0 16 16"><circle cx="8" cy="8" r="8" fill="var(--brown)"/><path d="M4.5 8.2 7 10.6 11.8 5.4" stroke="#fff" stroke-width="2" fill="none"/></svg>Gıda ile temasa uygundur.</li>
    </ul>

    <div class="wheat-art" role="img" aria-label="Buğday başakları ve buğday sapından pipetler illüstrasyonu"></div>

    <div class="badge">
      <svg class="arc" width="140" height="150" viewBox="0 0 140 150">
        <defs><path id="badge-arc" d="M14 74 A56 56 0 0 0 126 74"/></defs>
        <text font-family="Montserrat, sans-serif" font-size="13" fill="var(--brown)" letter-spacing="1">
          <textPath href="#badge-arc" startOffset="50%" text-anchor="middle">Tek kullanımlıktır</textPath>
        </text>
      </svg>
      <div class="count"><b>500</b><small>adet</small></div>
      <div class="size"><b>15</b><small>cm</small></div>
    </div>
  </div>
</body>
</html>
```